prestige web design for KESTRAL Finance

Hi Guys,

Looking to team up with a creative designer for another of our websites for KESTRAL finance.
if looking for our similar website www.brimwellfinance.com.au is one of our other companies. ideally working in our logo being black and white.

Please see attachments for our logo and a description
HOME
VEHICLE
EQUIPMENT
WHO WE ARE
CONTACT US

open to ideas on layout .

touch base if you have any questions.

Target Market(s)

Prestige cars and equipment -trucks earthmoving

Industry/Entity Type

finance

Coding

Coded - Design and coding required

Number of Pages Required

5+ page

Font styles to use
Sans Serif

Colors

Designer to choose colors to be used in the design.

```html
<!DOCTYPE html>
<html lang="en">
<head>
<meta charset="utf-8">
<title>KESTRAL Finance</title>
<link href="https://fonts.googleapis.com/css2?family=Lexend+Exa:wght@600;700&family=Montserrat:wght@400;500;600;700&family=Source+Sans+3:wght@400&display=swap" rel="stylesheet">
<style>
:root{
  --black:#050505;
  --ink:#111;
  --text:#333;
  --muted:#8a8a8a;
  --line:#bdbdbd;
  --page:#f9f9f9;
  --white:#fff;
  --shadow:#a9a9a9;
}
*{box-sizing:border-box;margin:0;padding:0}
html,body{width:1200px;height:3350px;overflow:hidden}
body{background:var(--page);font-family:'Montserrat',sans-serif;color:var(--text);position:relative}
.abs{position:absolute}
.backdrop{position:absolute;left:0;top:0;width:100%;height:100%}
.head-font{font-family:'Lexend Exa',sans-serif;font-weight:700;color:var(--ink);text-transform:uppercase}

/* header */
.site-header{position:absolute;left:0;top:0;width:1200px;height:79px;background:var(--black);border-bottom:1px solid #333;z-index:3}
.brand{position:absolute;display:flex;align-items:center;gap:10px;font-family:'Montserrat',sans-serif;white-space:nowrap}
.brand .name{font-weight:700;font-size:27px;color:var(--white);letter-spacing:.5px}
.brand .bar{width:2px;height:44px;background:var(--white)}
.brand .sub{font-weight:400;font-size:24px;color:var(--white)}
.main-nav a{position:absolute;top:33px;font-size:13px;color:var(--white);text-decoration:none;letter-spacing:.3px}
.main-nav a.active{font-weight:700}
.main-nav a.active::after{content:"";position:absolute;left:0;right:0;top:43px;height:2px;background:var(--white)}
.header-divider{position:absolute;left:970px;top:6px;width:1px;height:72px;background:#444}
.header-phone{position:absolute;left:1000px;top:30px;color:var(--white);font-weight:700;font-size:15px;display:flex;align-items:center;gap:6px}

/* hero */
.hero{position:absolute;left:0;top:0;width:1200px;height:660px}
.hero .backdrop{background:linear-gradient(100deg,#1a1d22 0%,#3a3f46 30%,#8d9199 55%,#4c5158 80%,#22252a 100%)}
.hero-title{position:absolute;top:180px;width:1200px;text-align:center;font-size:62px;color:var(--white);letter-spacing:6px}
.hero-sub{position:absolute;top:254px;width:1240px;text-align:center;font-family:'Source Sans 3',sans-serif;font-size:24px;color:var(--white)}
.hero-arrow{position:absolute;left:600px;top:552px}

/* calculator */
.calc{position:absolute;left:112px;top:600px;width:990px;height:275px;background:var(--white);box-shadow:0 3px 0 #d0d0d0}
.calc h2{position:absolute;top:38px;width:100%;text-align:center;font-family:'Montserrat',sans-serif;font-weight:600;font-size:25px;color:#222;padding-right:14px}
.field{position:absolute;border-bottom:1.5px solid var(--line)}
.field label{display:block;font-size:12px;color:var(--muted);margin-bottom:6px}
.field span{font-size:15px;font-weight:500;color:var(--ink)}
.btn-dark{position:absolute;left:668px;top:172px;width:268px;height:51px;background:var(--black);color:var(--white);font-weight:700;font-size:14px;letter-spacing:1.5px;display:flex;align-items:center;justify-content:center;gap:6px}

/* media blocks */
.photo{position:absolute}
.photo-shadow{position:absolute;background:var(--shadow)}
.copy{position:absolute;text-align:center;font-size:16.5px;line-height:28px;color:var(--text)}
.copy h2{font-size:29px;margin-bottom:10px;letter-spacing:1px}
.btn-outline{display:inline-block;border:2px solid var(--ink);padding:14px 30px;font-weight:700;font-size:13px;letter-spacing:1.5px;color:var(--ink);text-transform:uppercase}

/* service cards */
.service{position:absolute;top:1461px;width:502px;height:358px;text-align:center;overflow:hidden}
.service .inner{position:relative}
.service h3{font-size:25px;margin-top:12px}
.service p{font-size:16.5px;line-height:25px;margin:6px auto 14px;width:440px}
.service.light{left:99px;color:#444}
.service.light .backdrop{background:linear-gradient(160deg,#f4f4f4 0%,#dedede 55%,#c9c9c9 100%)}
.service.dark{left:614px;color:var(--white)}
.service.dark .backdrop{background:linear-gradient(160deg,#2c2a28 0%,#1f1f20 50%,#39393b 100%)}
.service.dark h3{color:var(--white)}
.service.dark .btn-outline{border-color:var(--white);color:var(--white)}
.service svg{margin-top:50px}

/* contact */
.contact{position:absolute;left:0;top:2442px;width:1200px;height:573px}
.contact .backdrop{background:linear-gradient(90deg,#1b1b1b 0%,#3a3a3a 45%,#2a2a2a 100%)}
.contact .intro{position:absolute;left:126px;top:152px;width:380px;color:var(--white);font-size:15.5px;line-height:28px}
.contact .intro h2{color:var(--white);font-size:29px;margin-bottom:22px}
.contact .intro .btn-outline{border-color:var(--white);color:var(--white);padding:12px 34px;margin-top:34px}
.form-card{position:absolute;left:551px;top:92px;width:546px;height:391px;background:var(--white)}
.form-card .field span{font-size:17px;font-weight:400;color:var(--text)}
.form-card .field label{font-size:13px}
.form-card .send{position:absolute;left:48px;top:312px;padding:11px 30px;font-size:12px;border-color:var(--ink);color:var(--ink)}

/* footer */
.site-footer .brand .name{color:var(--ink);font-size:34px}
.site-footer .brand .sub{color:var(--ink);font-size:28px}
.site-footer .brand .bar{background:var(--ink);height:50px}
.contact-item{position:absolute;top:3088px;display:flex;gap:12px;align-items:center}
.contact-item .lbl{font-size:13px;color:var(--ink)}
.contact-item .val{font-size:13px;font-weight:700;color:var(--ink);margin-top:4px}
.rule{position:absolute;left:8px;width:1184px;height:1px;background:#e2e2e2}
.foot-nav a{position:absolute;top:3208px;font-size:15px;color:var(--ink);text-decoration:none}
.copyright{position:absolute;top:3284px;left:469px;font-size:11px;color:#333}
.to-top{position:absolute;left:1044px;top:3273px;width:34px;height:34px;border-radius:50%;background:var(--ink)}
</style>
</head>
<body>

<section class="hero">
  <div class="backdrop" role="img" aria-label="Silver luxury SUV driving past city buildings"></div>
  <h1 class="hero-title head-font">Makers of Possible</h1>
  <p class="hero-sub">KESTRAL Finance has nearly 20 years industry experience</p>
  <svg class="hero-arrow" width="34" height="22" viewBox="0 0 34 22"><path d="M3 4l14 14L31 4" fill="none" stroke="#fff" stroke-width="3.5"/></svg>
</section>

<header class="site-header">
  <div class="brand" style="left:82px;top:17px"><span class="name">KESTRAL</span><span class="bar"></span><span class="sub">Finance</span></div>
  <nav class="main-nav">
    <a class="active" href="#" style="left:384px">HOME</a>
    <a href="#" style="left:475px">VEHICLE</a>
    <a href="#" style="left:581px">EQUIPMENT</a>
    <a href="#" style="left:710px">WHO WE ARE</a>
    <a href="#" style="left:849px">CONTACT US</a>
  </nav>
  <div class="header-divider"></div>
  <div class="header-phone">
    <svg width="18" height="18" viewBox="0 0 24 24"><path fill="#fff" d="M6.6 10.8a15.1 15.1 0 006.6 6.6l2.2-2.2a1 1 0 011-.25 11.4 11.4 0 003.6.57 1 1 0 011 1V20a1 1 0 01-1 1A17 17 0 013 4a1 1 0 011-1h3.5a1 1 0 011 1c0 1.25.2 2.45.57 3.57a1 1 0 01-.25 1z"/></svg>
    1300 418 2275
  </div>
</header>

<section class="calc">
  <h2>FINANCE REPAYMENT CALCULATOR</h2>
  <div class="field" style="left:52px;top:98px;width:272px;height:47px"><label>Purchase amount</label><span>$100000</span></div>
  <div class="field" style="left:345px;top:98px;width:274px;height:47px"><label>Deposit</label><span>$5000</span></div>
  <div class="field" style="left:669px;top:98px;width:272px;height:47px"><label>Balloon Payment</label><span>$2000</span></div>
  <div class="field" style="left:54px;top:164px;width:270px;height:53px"><label>Term</label><span>5 Year</span></div>
  <div class="field" style="left:345px;top:170px;width:274px;height:47px"><label>Interest rate% pa.</label><span>7.5</span></div>
  <div class="btn-dark">CALCULATE
    <svg width="20" height="14" viewBox="0 0 20 14"><path d="M0 7h18M12 1l6 6-6 6" fill="none" stroke="#fff" stroke-width="2"/></svg>
  </div>
</section>

<!-- about -->
<div class="photo-shadow" style="left:112px;top:1000px;width:471px;height:331px"></div>
<div class="photo" style="left:99px;top:985px;width:471px;height:333px;background:linear-gradient(120deg,#cfd4d4 0%,#6f7576 40%,#2d3a3a 70%,#86b3b0 100%)" role="img" aria-label="Smiling businessman working on a laptop"></div>
<div class="copy" style="left:630px;top:1006px;width:465px">
  <h2 class="head-font">Makers of Possible</h2>
  <p>KESTRAL Finance has nearly 20 years industry experience, so we certainly understand personal and business lending. We are committed to providing individuals and businesses with tailored financial services that enable them to reach and then exceed their financial goals.</p>
  <p style="margin-top:28px">We have a vast list of lenders to suit along with an online team ready to help you, so we're easily accessible and here when you need us.</p>
</div>

<!-- services -->
<article class="service light">
  <div class="backdrop" role="img" aria-label="Earthmoving loader on a gravel site"></div>
  <div class="inner">
    <svg width="52" height="52" viewBox="0 0 52 52" fill="none" stroke="#111" stroke-width="2.5"><rect x="7" y="4" width="38" height="38" rx="4"/><rect x="12" y="9" width="28" height="14"/><circle cx="16" cy="32" r="3"/><circle cx="36" cy="32" r="3"/><path d="M22 32h8M11 42v6h6v-6M35 42v6h6v-6M3 16h4M45 16h4"/></svg>
    <h3 class="head-font">Equipment</h3>
    <p>At KESTRAL, we help businesses of all sizes to secure funding in the form of a business loan for asset purchases from either a bank or private lender.</p>
    <span class="btn-outline">Apply Now</span>
  </div>
</article>
<article class="service dark">
  <div class="backdrop" role="img" aria-label="Dark SUV parked on a hillside"></div>
  <div class="inner">
    <svg width="62" height="44" viewBox="0 0 62 44" fill="none" stroke="#fff" stroke-width="2.2"><path d="M12 18l6-12h26l6 12M4 20h54v14H4zM8 34v6h8v-6M46 34v6h8v-6"/><circle cx="13" cy="27" r="3"/><circle cx="49" cy="27" r="3"/><path d="M22 28h18"/></svg>
    <h3 class="head-font">Vehicle Loan</h3>
    <p>While you focus on getting the right car, we will focus on getting you the right finance.</p>
    <span class="btn-outline">Apply Now</span>
  </div>
</article>

<!-- why -->
<div class="copy" style="left:110px;top:2060px;width:440px">
  <h2 class="head-font" style="margin-bottom:20px">Why choose us?</h2>
  <p style="font-size:17.5px;line-height:29px">Well, because we're here to help you! We care about outcomes AND helping you achieve a stress and enjoyable lending experience</p>
  <span class="btn-outline" style="margin-top:28px;padding:14px 32px">Learn More</span>
</div>
<div class="photo-shadow" style="left:652px;top:2050px;width:452px;height:306px"></div>
<div class="photo" style="left:617px;top:1995px;width:471px;height:348px;background:linear-gradient(90deg,#2a211b 0%,#8a5a2c 30%,#3a2a20 55%,#b07a45 75%,#2a2522 100%)" role="img" aria-label="Silver sports coupe in front of lit vertical panels"></div>

<!-- contact -->
<section class="contact">
  <div class="backdrop" role="img" aria-label="Monochrome city skyline"></div>
  <div class="intro">
    <h2 class="head-font">Contact KESTRAL</h2>
    <p>To find out how to get KESTRAL Finance working for you helping with your funding needs. Please call 13 47 21 &nbsp;( 13 KESTRAL)<br>Or Contact us now: Alternatively send us a message with your questions.</p>
    <span class="btn-outline">Call Us Now</span>
  </div>
  <form class="form-card">
    <div class="field" style="left:45px;top:58px;width:227px;height:45px"><label>First Name</label><span>Alex</span></div>
    <div class="field" style="left:290px;top:58px;width:227px;height:45px"><label>Last Name</label><span>Morgan</span></div>
    <div class="field" style="left:45px;top:134px;width:227px;height:55px"><label>Email address</label><span>alex@morgan.com</span></div>
    <div class="field" style="left:290px;top:134px;width:227px;height:55px"><label>Phone</label><span>+123 456 7890</span></div>
    <div class="field" style="left:45px;top:208px;width:472px;height:93px"><label>Message</label></div>
    <span class="btn-outline send">Send Message</span>
  </form>
</section>

<!-- footer -->
<footer class="site-footer">
  <div class="brand" style="left:122px;top:3072px"><span class="name">KESTRAL</span><span class="bar"></span><span class="sub">Finance</span></div>
  <div class="contact-item" style="left:480px">
    <svg width="32" height="32" viewBox="0 0 32 32"><circle cx="16" cy="16" r="16" fill="#bbb"/><path fill="#fff" d="M11.5 14.4a10 10 0 004.4 4.4l1.5-1.5a.7.7 0 01.7-.2 7.6 7.6 0 002.4.4.7.7 0 01.7.7v2.4a.7.7 0 01-.7.7A11.3 11.3 0 019 10.2a.7.7 0 01.7-.7h2.3a.7.7 0 01.7.7c0 .8.1 1.6.4 2.4a.7.7 0 01-.2.7z"/></svg>
    <div><div class="lbl">PHONE</div><div class="val">(123) 456 7890</div></div>
  </div>
  <div class="contact-item" style="left:668px">
    <svg width="32" height="32" viewBox="0 0 32 32"><circle cx="16" cy="16" r="16" fill="#bbb"/><rect x="9" y="11" width="14" height="10" fill="none" stroke="#fff" stroke-width="1.6"/><path d="M9 11l7 6 7-6" fill="none" stroke="#fff" stroke-width="1.6"/></svg>
    <div><div class="lbl">EMAIL</div><div class="val">hello@kestralfinance.com</div></div>
  </div>
  <div class="contact-item" style="left:904px">
    <svg width="32" height="32" viewBox="0 0 32 32"><circle cx="16" cy="16" r="16" fill="#bbb"/><path d="M16 24s-6-6-6-10a6 6 0 0112 0c0 4-6 10-6 10z" fill="#fff"/><circle cx="16" cy="14" r="2.2" fill="#bbb"/></svg>
    <div><div class="lbl">LOCATION</div><div class="val">City Address 123 Street</div></div>
  </div>
  <div class="rule" style="top:3178px"></div>
  <nav class="foot-nav">
    <a href="#" style="left:275px">HOME</a>
    <a href="#" style="left:410px">VEHICLE</a>
    <a href="#" style="left:562px">EQUIPMENT</a>
    <a href="#" style="left:740px">WHO WE ARE</a>
    <a href="#" style="left:928px">CONTACT US</a>
  </nav>
  <div class="rule" style="top:3259px"></div>
  <p class="copyright">© 2022 KESTRAL Finance | All Right Reserved</p>
  <div class="to-top"><svg width="34" height="34" viewBox="0 0 34 34"><path d="M11 20l6-6 6 6" fill="none" stroke="#fff" stroke-width="2"/></svg></div>
</footer>

</body>
</html>
```